QK-Deck Company Powerpoint Template

I would like to create a branded PowerPoint temple that my company can use for all presentations. our website is www.qk-deck-example.com. The company is a software provider for the auto recycling industry (junk yards). Our customers use our software to pull, process, and deliver orders to auto body shops and mechanic shops.
Pages that would be helpful:
Title Page
Content slide
Content slide with image
Workflow/flowchart slide
Image only slide
Final slide

Target Market(s)

Automotive Recycling

Industry/Entity Type

Automotive recycling software

Font styles to use
Sans Serif

Colors
0054AA
0677BA
7BADD7
CADEEF
E8F1F8
FFF300
FFF600
FEFA6F
FFFEC7
FFFEE8

Requirements
Must have
• similarities in other branded items like our website. Title Page, Content slide, Content slide with image, Workflow/flowchart slide, Image only slide, Final slide
Nice to have
• Simple clean design would be preferential

```html
<!DOCTYPE html>
<html lang="en">
<head>
<meta charset="utf-8">
<title>QK-Deck Presentation Template</title>
<link href="https://fonts.googleapis.com/css2?family=Lato:ital,wght@0,300;0,400;0,700;1,400&display=swap" rel="stylesheet">
<style>
  :root {
    --page-bg: #e5e5e5;
    --slide-bg: #ffffff;
    --brand: #0c5286;
    --brand-dark: #073a63;
    --ink: #333a40;
    --ink-soft: #5c6166;
    --muted: #8e9398;
    --rule: #b9bcbf;
  }
  * { box-sizing: border-box; margin: 0; padding: 0; }
  html, body { width: 696px; height: 1200px; overflow: hidden; }
  body { background: var(--page-bg); font-family: "Lato", sans-serif; color: var(--ink); position: relative; }

  .slide { position: absolute; left: 112px; width: 472px; height: 262px; background: var(--slide-bg); }
  .slide--cover { top: 64px; }
  .slide--vision { top: 335px; }
  .slide--list { top: 606px; }
  .slide--mission { top: 877px; }

  .brand-name { font-weight: 700; color: var(--brand); font-size: 15px; letter-spacing: .2px; display: flex; align-items: center; gap: 4px; }
  .brand-name .mark { width: 8px; height: 8px; background: var(--brand); }
  .slide-logo { position: absolute; left: 11px; top: 11px; }

  .cover-logo { position: absolute; top: 88px; left: 0; right: 0; justify-content: center; }
  .cover-title { position: absolute; top: 116px; left: 0; right: 0; text-align: center; font-size: 16px; font-weight: 700; color: var(--ink); }
  .cover-subtitle { position: absolute; top: 141px; left: 0; right: 0; text-align: center; font-size: 9px; color: var(--ink-soft); }
  .presenter { position: absolute; top: 182px; left: 0; right: 0; text-align: center; font-size: 10px; font-weight: 700; }
  .accent { color: var(--brand); }
  .cover-date { position: absolute; left: 22px; top: 239px; font-size: 7px; }
  .cover-site { position: absolute; right: 23px; top: 238px; font-size: 7px; }

  .title-bar { position: absolute; top: 22px; left: 50%; width: 18px; margin-left: -9px; height: 1.5px; background: var(--brand); }
  .slide-title { position: absolute; top: 25px; left: 0; right: 0; text-align: center; font-size: 16px; font-weight: 400; color: #1e2327; }
  .slide-subtitle { position: absolute; top: 47px; left: 0; right: 0; text-align: center; font-size: 5.5px; color: var(--brand); letter-spacing: .2px; }

  .slide-footer { position: absolute; left: 12px; right: 15px; top: 247px; display: flex; justify-content: space-between; font-size: 6.5px; }
  .page-no { color: var(--muted); }
  .page-no b { font-weight: 400; color: var(--ink); font-size: 7px; }

  .vision-box { position: absolute; left: 59px; top: 77px; width: 354px; height: 123px; border-radius: 2px;
    background: linear-gradient(135deg, #0b5287 0%, var(--brand-dark) 100%);
    box-shadow: 3px 5px 8px rgba(0,0,0,.25); color: #fff; text-align: center; }
  .vision-box .divider { position: absolute; top: 30px; left: 50%; width: 28px; margin-left: -14px; height: 1px; background: #fff; }
  .vision-text { position: absolute; top: 35px; left: 0; right: 0; font-style: italic; font-size: 10.5px; line-height: 19px; }

  .toc { position: absolute; top: 88px; left: 61px; display: grid; grid-template-columns: 144px 144px; column-gap: 61px; row-gap: 21.5px; }
  .toc-item { display: flex; justify-content: space-between; font-size: 6.5px; font-weight: 700; color: var(--ink-soft); padding: 0 2px 5px; border-bottom: 1.2px solid var(--rule); height: 12.5px; }
  .toc-item--active { color: var(--brand); border-bottom-color: var(--brand); }

  .mission-grid { position: absolute; top: 70px; left: 20px; width: 432px; display: grid; grid-template-columns: repeat(3, 120px); column-gap: 24px; row-gap: 6px; }
  .mission { height: 74px; text-align: center; padding-top: 14px; }
  .mission--featured { border: 0.6px solid #c9ccd0; border-radius: 2px; box-shadow: 0 4px 8px rgba(0,0,0,.12); }
  .mission h3 { font-size: 7.5px; font-weight: 400; color: var(--ink-soft); }
  .mission .dash { display: block; width: 8px; height: 1.3px; background: var(--brand); margin: 5px auto 6px; }
  .mission p { font-size: 4.6px; line-height: 8.4px; color: var(--muted); font-weight: 300; }
</style>
</head>
<body>

<section class="slide slide--cover">
  <div class="brand-name cover-logo"><span class="mark"></span>QK-Deck</div>
  <h1 class="cover-title">Presentation Tittle Goes Here</h1>
  <p class="cover-subtitle">Credential Subtittle Presentation</p>
  <p class="presenter">Mr. Alan <span class="accent">Marsh</span></p>
  <p class="cover-date">November <span class="accent">2022</span></p>
  <p class="cover-site"><span class="accent">qk-deck</span>.com</p>
</section>

<section class="slide slide--vision">
  <div class="brand-name slide-logo"><span class="mark"></span>QK-Deck</div>
  <span class="title-bar"></span>
  <h2 class="slide-title">Our Vission</h2>
  <div class="vision-box">
    <span class="divider"></span>
    <p class="vision-text">Lorem ipsum dolor sit amet, consectetuer adipiscing elit.<br>Maecenas porttitor congue massa. Fusce posuere, magna sed<br>pulvinar ultricies, purus lectus malesuada libero.</p>
  </div>
  <footer class="slide-footer"><span>qk-deck.com</span><span class="page-no">page <b>3</b></span></footer>
</section>

<section class="slide slide--list">
  <div class="brand-name slide-logo"><span class="mark"></span>QK-Deck</div>
  <span class="title-bar"></span>
  <h2 class="slide-title">Presentation List</h2>
  <p class="slide-subtitle">Here Our Credential Subtitile</p>
  <div class="toc">
    <div class="toc-item"><span>COVER SLIDES</span><span>01</span></div>
    <div class="toc-item"><span>INFOGRAPH ONE</span><span>07</span></div>
    <div class="toc-item toc-item--active"><span>PRESENTATION LIST</span><span>03</span></div>
    <div class="toc-item"><span>INFOGRAPH TWO</span><span>08</span></div>
    <div class="toc-item"><span>ABOUT US</span><span>04</span></div>
    <div class="toc-item"><span>INFOGRAPH THREE</span><span>09</span></div>
    <div class="toc-item"><span>OUR MISSIONS &amp; VISION</span><span>06</span></div>
    <div class="toc-item"><span>CLOSING SLIDES</span><span>10</span></div>
  </div>
  <footer class="slide-footer"><span>qk-deck.com</span><span class="page-no">page <b>2</b></span></footer>
</section>

<section class="slide slide--mission">
  <div class="brand-name slide-logo"><span class="mark"></span>QK-Deck</div>
  <span class="title-bar"></span>
  <h2 class="slide-title">Our Mission</h2>
  <div class="mission-grid">
    <article class="mission"><h3>Mission One</h3><span class="dash"></span><p>Lorem ipsum dolor sit amet, consecter<br>adipiscing eli Maecenas porttitor<br>adipiscing elit tam emotan.</p></article>
    <article class="mission mission--featured"><h3>Mission Two</h3><span class="dash"></span><p>Lorem ipsum dolor sit amet, consecter<br>adipiscing eli Maecenas porttitor<br>adipiscing elit tam emotan.</p></article>
    <article class="mission"><h3>Mission Three</h3><span class="dash"></span><p>Lorem ipsum dolor sit amet, consecter<br>adipiscing eli Maecenas porttitor<br>adipiscing elit tam emotan.</p></article>
    <article class="mission"><h3>Mission Four</h3><span class="dash"></span><p>Lorem ipsum dolor sit amet, consecter<br>adipiscing eli Maecenas porttitor<br>adipiscing elit tam emotan.</p></article>
    <article class="mission"><h3>Mission Five</h3><span class="dash"></span><p>Lorem ipsum dolor sit amet, consecter<br>adipiscing eli Maecenas porttitor<br>adipiscing elit tam emotan.</p></article>
    <article class="mission"><h3>Mission Six</h3><span class="dash"></span><p>Lorem ipsum dolor sit amet, consecter<br>adipiscing eli Maecenas porttitor<br>adipiscing elit tam emotan.</p></article>
  </div>
  <footer class="slide-footer"><span>qk-deck.com</span><span class="page-no">page <b>4</b></span></footer>
</section>

</body>
</html>
```